8" x 11" One Page Flyer for Fence Installation Company

We are looking to promote our business with a new flyer that would be handed out in person to people or put at their mailbox/door at their homes. The flyer needs to be creative and attention-grabbing. I have attached some of our previous flyers and our website information. Do not call or email regarding the flyer. We want the flyer to look professional but also friendly. One page, NOT folded. You can use images from our website at www.MyBraxtonYard.com or our Facebook page at www.Facebook.com/HollowbrookRailsBKT. We are flexible with what photos you can use but there must be photos of OUR fences on the flyer. More photos specifically can also be provided. Colors need to be suitable for a flyer printed on canary yellow in color paper OR white paper.

Target Market(s)

Homeowners that need a new fence

Industry/Entity Type

Construction

Font styles to use
Sans Serif
Other font styles liked:
• HD Colton

Colors
0054AA
0677BA
7BADD7
CADEEF
E8F1F8
0094D4
00A9DD
6FCCEA
C7EBF8
E9F6FB

Requirements
Must have
• Our fence photos - mostly wood fence photos (different designs), SIZE SHOULD BE LETTER SIZE 8" x 11"
Nice to have
• A nice bible verse featured at the bottom of the flyer.
Should not have
• DO NOT COPY THE WEBSITE FORMAT, I WANT SOMETHING UNIQUE. Other people's fence photos, they must all come from our website or facebook page

```html
<!DOCTYPE html>
<html lang="en">
<head>
<meta charset="utf-8">
<title>Hollowbrook Rails Flyer</title>
<link href="https://fonts.googleapis.com/css2?family=Inter:ital,wght@0,400;0,500;0,600;0,700;1,400;1,500&display=swap" rel="stylesheet">
<style>
  :root {
    --stage: #dbe6ef;
    --brand-blue: #1577bd;
    --brand-blue-deep: #0f62aa;
    --accent-orange: #f4a127;
    --paper: #f7f7f7;
    --ink: #2b2b2b;
    --heading-blue: #1a78c2;
    --white: #ffffff;
  }
  * { box-sizing: border-box; margin: 0; padding: 0; }
  html, body { width: 1200px; height: 800px; overflow: hidden; }
  body {
    background: var(--stage);
    font-family: "Inter", Arial, sans-serif;
    color: var(--ink);
    position: relative;
  }
  .flyer {
    position: absolute;
    left: 305px; top: 18px;
    width: 590px; height: 764px;
    background: var(--paper);
    box-shadow: 0 10px 30px rgba(40, 70, 100, 0.18);
    overflow: hidden;
  }
  .masthead {
    height: 200px;
    background: linear-gradient(135deg, var(--brand-blue) 60%, var(--brand-blue-deep));
    padding: 26px 34px 0;
    color: var(--white);
    border-bottom: 8px solid var(--accent-orange);
  }
  .brand { display: flex; align-items: center; gap: 12px; }
  .brand-mark { width: 26px; height: 26px; background: var(--white); border-radius: 3px; }
  .brand-name { font-size: 26px; font-weight: 600; letter-spacing: -0.3px; line-height: 1; }
  .brand-tagline {
    font-size: 5.5px; letter-spacing: 1.4px; text-transform: uppercase;
    margin: 4px 0 0 38px; opacity: 0.9;
  }
  .headline {
    margin-top: 22px;
    font-size: 37px; font-weight: 400; line-height: 1.12; letter-spacing: -1.4px;
  }
  .headline strong { font-weight: 700; }
  .info {
    position: absolute; left: 0; right: 0; top: 200px;
    display: flex; padding: 22px 34px 0;
  }
  .location { width: 226px; }
  .section-title {
    color: var(--heading-blue); font-size: 18px; font-weight: 500; letter-spacing: -0.6px; line-height: 1.2;
  }
  .address { font-size: 9px; margin-top: 5px; letter-spacing: -0.3px; }
  .map {
    margin-top: 12px; width: 196px; height: 118px;
    background: linear-gradient(135deg, #e6e9ec, #d9dee2);
  }
  .showroom { margin-top: 10px; font-size: 10px; font-style: italic; letter-spacing: -0.4px; line-height: 1.4; }
  .showroom p + p { margin-top: 6px; }
  .hours { color: var(--heading-blue); font-weight: 500; }
  .benefits { flex: 1; padding-left: 48px; padding-top: 10px; }
  .benefits .section-title { font-size: 20px; font-weight: 600; }
  .benefits-lead { margin-top: 8px; font-size: 11.5px; line-height: 1.35; letter-spacing: -0.4px; width: 210px; }
  .benefit-list { list-style: none; margin-top: 9px; }
  .benefit-list li {
    font-size: 11.5px; line-height: 14px; letter-spacing: -0.4px; margin-bottom: 7px;
    display: flex; align-items: center; gap: 10px;
  }
  .benefit-list li::before {
    content: ""; width: 5px; height: 5px; border-radius: 50%;
    background: var(--accent-orange); flex: none;
  }
  .gallery {
    position: absolute; left: 34px; top: 514px; width: 522px; height: 176px;
    display: grid; grid-template-columns: 150px 1fr 1.3fr; grid-template-rows: 1fr 1fr; gap: 4px;
  }
  .photo { width: 100%; height: 100%; }
  .photo-deck { grid-row: 1 / 3; background: linear-gradient(160deg, #6f8a4e, #8b5a32 70%, #6b4026); }
  .photo-privacy { background: linear-gradient(180deg, #c9cfd6 10%, #c9a66e 45%, #7f9b4a); }
  .photo-shed { background: linear-gradient(180deg, #5f7f3e, #d7cf9c 55%, #5b7a37); }
  .photo-neighbourhood { background: linear-gradient(180deg, #c6d3e2 20%, #d8c38f 55%, #7e9a4c); }
  .photo-iron { background: linear-gradient(180deg, #6d8a46, #e4e4e4 40%, #2e3328 65%, #6d8f3f); }
  .contact-bar {
    position: absolute; left: 0; right: 0; bottom: 0; height: 60px;
    background: linear-gradient(90deg, var(--brand-blue), var(--brand-blue-deep));
    border-top: 6px solid var(--accent-orange);
    display: flex; align-items: center; justify-content: center; gap: 16px;
    color: var(--white); font-size: 11.5px; font-style: italic; letter-spacing: -0.3px;
  }
  .contact-item { display: flex; align-items: center; gap: 6px; }
  .contact-item svg { width: 12px; height: 12px; flex: none; }
  .divider { width: 1px; height: 18px; background: var(--white); opacity: 0.85; }
</style>
</head>
<body>
  <main class="flyer">
    <header class="masthead">
      <div class="brand">
        <span class="brand-mark"></span>
        <span class="brand-name">Hollowbrook Rails</span>
      </div>
      <p class="brand-tagline">"Because good fences make good neighbours"</p>
      <h1 class="headline"><strong>We build fences,</strong> and we would<br>love to build your fence too!</h1>
    </header>

    <section class="info">
      <div class="location">
        <h2 class="section-title">Where are we?</h2>
        <p class="address">418 Kestrel Rd Alderton, NC 28990</p>
        <div class="map" role="img" aria-label="Street map showing the showroom location"></div>
        <div class="showroom">
          <p>Visit our indoor &amp; outdoor showroom!</p>
          <p>Our outdoor showroom is open 24/7, while our indoor showroom and office is open <span class="hours">Mon-Thu 9AM - 3PM, Friday 9AM - 1PM</span></p>
        </div>
      </div>
      <div class="benefits">
        <h2 class="section-title">Why choose us?</h2>
        <p class="benefits-lead">Beautiful, professionally installed fences at affordable prices!</p>
        <ul class="benefit-list">
          <li>Free Estimates</li>
          <li>Professional Installation</li>
          <li>Concrete in EVERY Post</li>
          <li>HOA Submission Assistance</li>
          <li>Lifetime Workmanship Warranty</li>
          <li>Experienced Installation Teams</li>
          <li>Quality Workmanship &amp; Materials</li>
          <li>FREE Gate Adjustments for LIFE</li>
        </ul>
      </div>
    </section>

    <section class="gallery">
      <div class="photo photo-deck" role="img" aria-label="Wooden scalloped picket fence seen from a backyard deck"></div>
      <div class="photo photo-privacy" role="img" aria-label="Tall wooden privacy fence beside a house"></div>
      <div class="photo photo-neighbourhood" role="img" aria-label="Long wooden fence along a suburban lawn"></div>
      <div class="photo photo-shed" role="img" aria-label="Small wooden picket enclosure in a garden"></div>
      <div class="photo photo-iron" role="img" aria-label="Black metal fence around a green yard"></div>
    </section>

    <footer class="contact-bar">
      <span class="contact-item">
        <svg viewBox="0 0 24 24" fill="none" stroke="currentColor" stroke-width="2"><circle cx="12" cy="12" r="10"/><path d="M2 12h20M12 2c3 3 3 17 0 20M12 2c-3 3-3 17 0 20"/></svg>
        MyBraxtonYard.com
      </span>
      <span class="divider"></span>
      <span class="contact-item">
        <svg viewBox="0 0 24 24" fill="currentColor"><path d="M6.6 10.8a15.1 15.1 0 0 0 6.6 6.6l2.2-2.2a1 1 0 0 1 1-.25 11.4 11.4 0 0 0 3.6.57 1 1 0 0 1 1 1V20a1 1 0 0 1-1 1A17 17 0 0 1 3 4a1 1 0 0 1 1-1h3.5a1 1 0 0 1 1 1c0 1.25.2 2.45.57 3.57a1 1 0 0 1-.25 1z"/></svg>
        555-014-2290
      </span>
      <span class="divider"></span>
      <span class="contact-item">
        <svg viewBox="0 0 24 24" fill="currentColor"><path d="M2 5h20v14H2z"/><path d="M2 5l10 8 10-8" fill="none" stroke="#1577bd" stroke-width="2"/></svg>
        office@mybraxtonyard.com
      </span>
    </footer>
  </main>
</body>
</html>
```